Arabic Alphabet Art Contest

Arabic Studies at Brookhaven

Arabic Art Contest

Express yourselves through Arabic Art

Calling all student artists to participate in Brookhaven's 1st Arabic Art Contest

The Arabic Alphabet is made up of 28 letters. Let's see you artistic skills by creating a poster with all of the Arabic Alphabets

Art Submissions due by: February 1st, 2021
Submit all entries to Mr. Qudsi

Grade Prize: $100 Vendrix Gift Card
Second Prize: $75 Vendrix Gift Card
3rd Prize: $50 Vendrix Gift Card
4th Prize: $25 Gift Card

```html
<!DOCTYPE html>
<html lang="en">
<head>
<meta charset="utf-8">
<title>Brookhaven's 1st Arabic Art Contest</title>
<link rel="stylesheet" href="https://fonts.googleapis.com/css2?family=Berkshire+Swash&family=Caveat:wght@600&family=Josefin+Sans:wght@700&family=Poppins:wght@400;600;700;800&family=Libre+Baskerville:wght@700&display=swap">
<style>
  :root {
    --paper: #ffffff;
    --plum: #7a2780;
    --plum-dark: #5e2266;
    --teal: #1f9e8c;
    --teal-panel: #25a594;
    --rust: #b5541c;
    --ink: #111111;
    --mandala-purple: #7d4b7e;
    --mandala-teal: #2aa7a0;
    --mandala-peach: #f6b98a;
    --mandala-pink: #e56b86;
  }
  * { margin: 0; padding: 0; box-sizing: border-box; }
  html, body { width: 849px; height: 1200px; overflow: hidden; background: var(--paper); }
  .poster {
    position: relative; width: 849px; height: 1200px; overflow: hidden;
    background: var(--paper); font-family: "Poppins", sans-serif; color: var(--ink);
  }
  .ornament { position: absolute; }
  .ornament--top-left {
    left: -40px; top: -60px; width: 320px; height: 240px; border-radius: 50%;
    background: radial-gradient(circle at 45% 45%, var(--mandala-pink) 0 10%, var(--mandala-peach) 11% 30%, var(--mandala-teal) 31% 52%, var(--mandala-purple) 53% 70%, transparent 71%);
  }
  .ornament--top-right {
    right: -311px; top: -220px; width: 520px; height: 520px; border-radius: 50%;
    background: radial-gradient(circle closest-side, var(--mandala-pink) 0 14%, var(--mandala-peach) 15% 40%, var(--mandala-teal) 41% 65%, var(--mandala-purple) 66% 99%, transparent 100%);
  }
  .ornament--faint-left {
    left: -180px; top: 280px; width: 500px; height: 700px; border-radius: 50%; opacity: .16;
    background: radial-gradient(circle, var(--mandala-pink) 0 10%, var(--mandala-peach) 11% 30%, var(--mandala-teal) 31% 50%, var(--mandala-purple) 51% 66%, transparent 67%);
  }
  .ornament--faint-right {
    right: -200px; bottom: -120px; width: 480px; height: 560px; border-radius: 50%; opacity: .16;
    background: radial-gradient(circle, var(--mandala-pink) 0 10%, var(--mandala-peach) 11% 30%, var(--mandala-teal) 31% 50%, var(--mandala-purple) 51% 66%, transparent 67%);
  }
  .brand {
    position: absolute; left: 0; right: 0; top: 62px;
    display: flex; align-items: center; justify-content: center; gap: 8px;
    font-family: "Libre Baskerville", serif; font-weight: 700; font-size: 18px; color: var(--plum-dark);
  }
  .brand__mark { width: 14px; height: 14px; background: var(--plum-dark); }
  .department {
    position: absolute; left: 0; right: 0; top: 138px; text-align: center;
    font-family: "Libre Baskerville", serif; font-weight: 700; font-size: 12.5px; color: var(--ink);
  }
  .kicker {
    position: absolute; left: 0; right: 0; top: 203px; text-align: center;
    font-family: "Josefin Sans", sans-serif; font-weight: 700; font-size: 23px;
    letter-spacing: 3px; color: var(--plum-dark);
  }
  .title {
    position: absolute; left: 0; right: 0; top: 226px; text-align: center;
    font-family: "Berkshire Swash", cursive; font-weight: 400; color: var(--plum); line-height: 1;
  }
  .title__line { display: block; }
  .title__line--first { font-size: 100px; }
  .title__line--second { font-size: 138px; margin-top: -24px; }
  .tagline {
    position: absolute; left: 0; right: 0; top: 454px; text-align: center;
    font-family: "Caveat", cursive; font-weight: 600; font-size: 35px; color: var(--rust);
  }
  .callout {
    position: absolute; left: 0; right: 0; top: 580px; text-align: center;
    font-weight: 700; font-size: 20px; color: var(--teal);
  }
  .brief {
    position: absolute; left: 116px; top: 627px; width: 617px; height: 179px;
    background: var(--teal-panel); border-radius: 22px;
  }
  .brief__icon { position: absolute; left: 16px; top: 42px; width: 78px; height: 88px; }
  .brief__text {
    position: absolute; left: 106px; top: 26px; width: 488px;
    color: #fff; font-size: 21px; line-height: 38px; font-weight: 400;
  }
  .brief__text strong { font-weight: 700; }
  .grand-prize { position: absolute; left: 140px; top: 852px; width: 192px; text-align: center; }
  .grand-prize__label { font-weight: 800; font-size: 24px; letter-spacing: .3px; line-height: 1; }
  .grand-prize__amount { font-weight: 800; font-size: 82px; line-height: 1; margin-top: 2px; letter-spacing: -2px; }
  .grand-prize__reward { font-size: 18px; margin-top: -2px; }
  .prize-list { position: absolute; left: 354px; top: 855px; list-style: none; font-size: 27px; line-height: 42px; }
  .prize-list strong { font-weight: 800; }
  .deadline { position: absolute; left: 0; right: 0; top: 1028px; text-align: center; }
  .deadline__label { font-weight: 700; font-size: 28px; color: var(--teal); line-height: 34px; }
  .deadline__date { font-weight: 700; font-size: 36px; color: var(--plum-dark); line-height: 40px; }
  .deadline__contact { font-weight: 700; font-size: 21px; color: var(--teal); line-height: 30px; margin-top: 10px; }
  .deadline__contact span { color: var(--plum-dark); }
</style>
</head>
<body>
<main class="poster">
  <div class="ornament ornament--faint-left" role="img" aria-label="Faint mandala ornament in pastel tones"></div>
  <div class="ornament ornament--faint-right" role="img" aria-label="Faint mandala ornament in pastel tones"></div>
  <div class="ornament ornament--top-left" role="img" aria-label="Colourful mandala ornament in purple, teal, peach and pink"></div>
  <div class="ornament ornament--top-right" role="img" aria-label="Colourful mandala ornament in purple, teal, peach and pink"></div>

  <header>
    <div class="brand"><span class="brand__mark"></span>Brookhaven</div>
    <p class="department">Arabic Studies at Brookhaven</p>
    <p class="kicker">THE BROOKHAVEN'S 1ST</p>
    <h1 class="title">
      <span class="title__line title__line--first">Arabic Art</span>
      <span class="title__line title__line--second">Contest</span>
    </h1>
    <p class="tagline">"Express yourselves through Arabic Art"</p>
  </header>

  <p class="callout">Calling all student artists to participate!</p>

  <section class="brief">
    <svg class="brief__icon" viewBox="0 0 78 88" aria-hidden="true">
      <rect x="8" y="4" width="64" height="80" rx="4" fill="#fdf6e3" stroke="#333" stroke-width="2.5"/>
      <rect x="2" y="72" width="20" height="14" rx="3" fill="#f3e6c4" stroke="#333" stroke-width="2.5"/>
      <rect x="56" y="2" width="20" height="12" rx="3" fill="#f3e6c4" stroke="#333" stroke-width="2.5"/>
      <g stroke="#333" stroke-width="2.5" stroke-linecap="round">
        <line x1="18" y1="24" x2="22" y2="24"/><line x1="28" y1="24" x2="60" y2="24"/>
        <line x1="18" y1="36" x2="22" y2="36"/><line x1="28" y1="36" x2="60" y2="36"/>
        <line x1="18" y1="48" x2="22" y2="48"/><line x1="28" y1="48" x2="60" y2="48"/>
        <line x1="18" y1="60" x2="22" y2="60"/><line x1="28" y1="60" x2="60" y2="60"/>
      </g>
    </svg>
    <p class="brief__text">The Arabic Alphabet is made up of 28 letters. Let's see your artistic skills by <strong>creating a poster</strong> with all of the <strong>Arabic Alphabets.</strong></p>
  </section>

  <section class="prizes">
    <div class="grand-prize">
      <p class="grand-prize__label">GRAND PRIZE</p>
      <p class="grand-prize__amount">$100</p>
      <p class="grand-prize__reward">Vendrix Gift Card</p>
    </div>
    <ul class="prize-list">
      <li>2nd: <strong>$75</strong> Vendrix Gift Card</li>
      <li>3rd:&nbsp; <strong>$50</strong> Vendrix Gift Card</li>
      <li>4th:&nbsp; <strong>$25</strong> Vendrix Gift Card</li>
    </ul>
  </section>

  <footer class="deadline">
    <p class="deadline__label">Art Submissions due by:</p>
    <p class="deadline__date">February 1st, 2021</p>
    <p class="deadline__contact">Submit all entries to <span>Mr. Qudsi</span></p>
  </footer>
</main>
</body>
</html>
```